Tallgrove Vale Management

I need a professional website. My current website is tallgrovevalemanagement.com and I hate it. It was created with some AI tool very quickly because I needed a site up and running with no advanced notice. I’m open to all designs .. I trust you, the professionals will deliver the results I’m anxiously awaiting! :)

```html
<!DOCTYPE html>
<html lang="en">
<head>
<meta charset="utf-8">
<title>Tallgrove Vale Management</title>
<link href="https://fonts.googleapis.com/css2?family=Outfit:wght@500;600;700&family=Roboto:wght@400;500;700&display=swap" rel="stylesheet">
<style>
:root{
  --navy:#2c3b66;
  --navy-dark:#1f2b4d;
  --red:#e3262f;
  --text:#555a66;
  --white:#ffffff;
  --line:#d9dbe0;
}
*{margin:0;padding:0;box-sizing:border-box}
html,body{width:1200px;height:4037px;overflow:hidden}
body{position:relative;background:var(--white);font-family:Roboto,sans-serif;color:var(--text)}
.abs{position:absolute}
.heading{font-family:Outfit,sans-serif;font-weight:600;text-transform:uppercase;color:var(--navy);line-height:1.2}
.heading .accent{color:var(--red)}
.btn{position:absolute;display:flex;align-items:center;justify-content:center;gap:8px;background:var(--red);color:var(--white);font:700 15px Roboto,sans-serif;text-transform:uppercase;letter-spacing:.3px}
.btn .dot{width:13px;height:13px;border-radius:50%;background:var(--white);position:relative}
.btn .dot::after{content:"";position:absolute;left:4px;top:3.5px;border-left:5px solid var(--red);border-top:3px solid transparent;border-bottom:3px solid transparent}
.brand{font-family:Outfit,sans-serif;font-weight:700;text-transform:uppercase;color:var(--white);text-align:center;line-height:1.1}
/* hero */
.hero-photo{left:0;top:0;width:1200px;height:720px;background:linear-gradient(180deg,#5a4a78 0%,#a85d5a 22%,#c97a4c 32%,#3b4770 55%,#2a3a5e 75%,#1c2440 100%)}
.nav{top:74px;left:398px;display:flex;gap:26px;font:500 14px Roboto,sans-serif;color:var(--white);text-transform:uppercase}
.nav .active{color:var(--red)}
.nav-cta{left:883px;top:62px;width:204px;height:45px;font-size:15px}
.hero-logo{left:113px;top:28px;width:124px;height:116px;display:flex;align-items:center;justify-content:center;gap:8px}
.hero-eyebrow{left:0;width:1200px;top:216px;text-align:center;font:500 21px Outfit,sans-serif;color:var(--white);text-transform:uppercase}
.hero-title{left:0;width:1200px;top:250px;text-align:center;font:700 51px/56px Outfit,sans-serif;color:var(--white);text-transform:uppercase}
.hero-frame{left:700px;top:228px;width:206px;height:120px;border-top:2px solid var(--navy);border-right:2px solid var(--navy)}
.hero-cta{left:519px;top:389px;width:162px;height:45px}
/* expertise */
.expertise-mark{left:94px;top:752px;width:501px;height:520px;display:flex;flex-direction:column;align-items:center;justify-content:center;gap:22px}
.expertise-mark .sq{width:90px;height:90px;background:var(--navy)}
.expertise-mark .name{font:700 46px/1.1 Outfit,sans-serif;color:var(--navy);text-transform:uppercase;text-align:center}
.expertise-title{left:668px;top:808px;font-size:35px}
.body-copy{font-size:14px;line-height:24px;color:var(--text)}
.expertise-copy{left:668px;top:918px;width:415px}
.expertise-copy p+p{margin-top:14px}
/* solutions */
.section-title{left:0;width:1200px;text-align:center;font-size:35px}
.title-rule{left:550px;top:1432px;width:100px;height:3px;background:var(--red)}
.card{top:1493px;width:400px;height:362px}
.card svg{position:absolute;left:0;top:0}
.card-inner{position:absolute;left:0;top:0;width:400px;text-align:center;color:var(--white)}
.card-icon{position:absolute;left:164px;top:38px;width:72px;height:72px;border-radius:50%;background:var(--white)}
.card-icon svg{left:22px;top:20px}
.card h3{position:absolute;top:138px;width:400px;font:700 19px Roboto,sans-serif}
.card .price{position:absolute;top:166px;width:400px;font:500 18px Roboto,sans-serif}
.card p{position:absolute;top:205px;left:45px;width:310px;font-size:13px;line-height:21.5px}
.card .more{position:absolute;top:312px;width:400px;font:700 13px Roboto,sans-serif;text-transform:uppercase}
.card.navy .price,.card.navy .more{color:var(--red)}
/* about */
.about-title{left:111px;top:1982px;font-size:36px;line-height:40px}
.about-copy{left:111px;top:2126px;width:410px;text-align:justify}
.about-copy p+p{margin-top:12px}
.about-photo{left:600px;top:1963px;width:481px;height:478px;background:linear-gradient(135deg,#e9e6e1 0%,#d8cfc4 40%,#b8874e 60%,#e7e3de 100%)}
.about-badge{left:935px;top:2320px;width:148px;height:100px;background:var(--navy);border:5px solid var(--white);display:flex;align-items:center;justify-content:center}
.about-badge .brand{font-size:17px}
/* testimonials */
.t-card{top:2763px;width:407px;height:230px;background:var(--white);border-radius:28px;box-shadow:0 6px 12px rgba(30,40,70,.18)}
.t-quote{position:absolute;left:100px;top:20px;font:700 56px/1 Outfit,sans-serif;color:var(--red)}
.t-text{position:absolute;left:102px;top:82px;width:270px;font-size:13px;line-height:23px;color:#777}
.t-name{position:absolute;left:102px;top:160px;font:500 16px Roboto,sans-serif;color:#222}
.t-stars{position:absolute;left:102px;top:181px;display:flex;gap:3px}
.avatar{width:116px;height:116px;border-radius:50%;border:3px solid var(--white);background:linear-gradient(160deg,#9aa3b2,#3e4658)}
.arrow{top:2860px}
/* contact */
.contact-bg{left:0;top:3107px;width:1200px;height:597px}
.contact-title{left:111px;top:3214px;font-size:36px;color:var(--white)}
.field{background:var(--white);font-size:13px;color:#666;padding:12px 13px}
.contact-frame{left:648px;top:3196px;width:407px;height:60px;border:3px solid var(--white);border-bottom:none}
.contact-photo{left:663px;top:3209px;width:453px;height:395px;background:linear-gradient(135deg,#3b3f3a 0%,#6f6a5c 40%,#c9c2b2 70%,#8a9a84 100%)}
.contact-frame-b{left:1116px;top:3400px;width:9px;height:226px;background:var(--white)}
.contact-frame-c{left:760px;top:3604px;width:365px;height:22px;border-bottom:9px solid var(--white)}
.contact-badge{left:631px;top:3264px;width:107px;height:97px;background:var(--white);border-radius:6px;display:flex;align-items:center;justify-content:center}
.contact-badge .brand{color:var(--navy);font-size:14px}
/* footer */
.footer-logo{left:149px;top:3761px;width:172px;height:177px;display:flex;flex-direction:column;align-items:center;justify-content:center;gap:10px}
.footer-logo .sq{width:44px;height:44px;background:var(--navy)}
.footer-logo .brand{color:var(--navy);font-size:20px}
.vline{width:1px;background:var(--line)}
.vline::before{content:"";position:absolute;left:-2px;top:0;width:5px;height:46px;background:var(--red)}
.f-title{font:500 15px Roboto,sans-serif;color:#222;text-transform:uppercase}
.f-links{font-size:13.5px;line-height:25px;color:#444;list-style:none}
.f-info{font-size:14px;line-height:22px;color:#333}
.f-rule{left:111px;top:3960px;width:978px;height:1px;background:var(--line)}
.f-legal{top:3986px;font-size:13px;color:#444}
.social{top:3979px;width:30px;height:30px;border-radius:50%;border:1px solid #aaa}
.social::after{content:"";position:absolute;left:11px;top:11px;width:6px;height:6px;border-radius:50%;background:#555}
</style>
</head>
<body>

<!-- hero -->
<div class="abs hero-photo" role="img" aria-label="City skyline at dusk reflected on a river"></div>
<svg class="abs" style="left:0;top:530px" width="1200" height="200" viewBox="0 0 1200 200">
  <polyline points="0,18 600,173 1200,18" fill="none" stroke="#2c3b66" stroke-width="16"/>
  <polygon points="0,32 600,187 1200,32 1200,200 0,200" fill="#ffffff"/>
</svg>
<div class="abs hero-logo"><div class="brand" style="font-size:17px">Tallgrove<br>Vale</div></div>
<nav class="abs nav"><span class="active">Home</span><span>About Us</span><span>Our Services</span><span>Blog</span><span>Contact Us</span></nav>
<div class="btn nav-cta">Request a Proposal</div>
<div class="abs hero-frame"></div>
<div class="abs hero-eyebrow">Tallgrove Vale Management</div>
<h1 class="abs hero-title">A True Partner, Not<br>Just a Vendor.</h1>
<div class="btn hero-cta">Contact Us</div>

<!-- expertise -->
<div class="abs expertise-mark"><div class="sq"></div><div class="name">Tallgrove<br>Vale<br>Management</div></div>
<h2 class="abs heading expertise-title">Expertise Rooted In<br><span class="accent">Asset Preservation</span></h2>
<div class="abs body-copy expertise-copy">
  <p>The organization applies rigorously tested frameworks and data-driven methodologies to safeguard property value while elevating tenant experience.</p>
  <p>Drawing on decades of collective expertise, the team facilitates regulatory compliance, cost efficiency, and proactive maintenance. This disciplined approach enables owners to preserve capital, enhance occupancy rates, and demonstrate long-term resilience across diverse market conditions.</p>
</div>
<div class="btn" style="left:669px;top:1158px;width:169px;height:52px">Learn More <span class="dot"></span></div>

<!-- solutions -->
<h2 class="abs heading section-title" style="top:1378px">Strategic Property <span class="accent">Management Solutions</span></h2>
<div class="abs title-rule"></div>

<div class="abs card navy" style="left:0">
  <svg width="400" height="362"><polygon points="0,113 200,0 400,113 400,362 0,362" fill="#2c3b66"/></svg>
  <div class="card-inner">
    <div class="card-icon"><svg width="28" height="32" viewBox="0 0 28 32"><rect x="7" y="2" width="14" height="16" fill="none" stroke="#2c3b66" stroke-width="2"/><path d="M2 24h10l6 4h8" fill="none" stroke="#2c3b66" stroke-width="2"/></svg></div>
    <h3>Basic Service</h3><div class="price">$99.00</div>
    <p>Describe important details like price, value, length of service, and why it's unique. Or use these sections to showcase different key values of your products or services.</p>
    <div class="more">Learn More &raquo;</div>
  </div>
</div>
<div class="abs card red" style="left:400px">
  <svg width="400" height="362"><polygon points="0,113 200,0 400,113 400,362 0,362" fill="#e3262f"/></svg>
  <div class="card-inner">
    <div class="card-icon"><svg width="28" height="32" viewBox="0 0 28 32"><rect x="2" y="4" width="24" height="24" fill="none" stroke="#e3262f" stroke-width="2"/><path d="M6 12h16M6 18h10" stroke="#e3262f" stroke-width="2"/></svg></div>
    <h3>Basic Service</h3><div class="price">$99.00</div>
    <p>Describe important details like price, value, length of service, and why it's unique. Or use these sections to showcase different key values of your products or services.</p>
    <div class="more">Learn More &raquo;</div>
  </div>
</div>
<div class="abs card navy" style="left:800px">
  <svg width="400" height="362"><polygon points="0,113 200,0 400,113 400,362 0,362" fill="#2c3b66"/></svg>
  <div class="card-inner">
    <div class="card-icon"><svg width="28" height="32" viewBox="0 0 28 32"><path d="M2 16 14 4l12 12v14H2z" fill="none" stroke="#2c3b66" stroke-width="2"/><circle cx="14" cy="19" r="4" fill="none" stroke="#2c3b66" stroke-width="2"/></svg></div>
    <h3>Basic Service</h3><div class="price">$99.00</div>
    <p>Describe important details like price, value, length of service, and why it's unique. Or use these sections to showcase different key values of your products or services.</p>
    <div class="more">Learn More &raquo;</div>
  </div>
</div>

<!-- about -->
<h2 class="abs heading about-title">About Our Property<br><span class="accent">Management<br>Solutions</span></h2>
<div class="abs body-copy about-copy">
  <p>Our organization delivers comprehensive property management solutions that optimize asset performance and tenant satisfaction. By integrating advanced analytics with proven operational frameworks, our specialists ensure each property achieves sustained value appreciation.</p>
  <p>Drawing on decades of collective expertise, the team facilitates regulatory compliance, cost efficiency, and proactive maintenance.</p>
</div>
<div class="btn" style="left:111px;top:2366px;width:170px;height:50px">Learn More <span class="dot"></span></div>
<div class="abs about-photo" role="img" aria-label="Agent with clipboard handing keys to a smiling couple"></div>
<div class="abs about-badge"><div class="brand">Tallgrove<br>Vale</div></div>

<!-- testimonials -->
<svg class="abs" style="left:0;top:2570px" width="1200" height="537" viewBox="0 0 1200 537" role="img" aria-label="Faded suburban houses with people in the background">
  <defs><linearGradient id="tbg" x1="0" y1="0" x2="0" y2="1"><stop offset="0" stop-color="#dfe2e9"/><stop offset="1" stop-color="#e8e9ee"/></linearGradient></defs>
  <polygon points="0,78 600,0 1200,78 1200,537 0,537" fill="url(#tbg)"/>
</svg>
<h2 class="abs heading section-title" style="top:2667px"><span class="accent">Client</span> Testimonials</h2>
<svg class="abs arrow" style="left:38px" width="24" height="34"><polyline points="20,3 5,17 20,31" fill="none" stroke="#9aa0ab" stroke-width="3"/></svg>
<svg class="abs arrow" style="left:1136px" width="24" height="34"><polyline points="4,3 19,17 4,31" fill="none" stroke="#9aa0ab" stroke-width="3"/></svg>

<div class="abs t-card" style="left:168px">
  <div class="t-quote">&ldquo;</div>
  <p class="t-text">Lorem ipsum dolor sit amet, consectetur adipiscing elit, sed do eiusmod tempor incididunt dolore magna aliqua.</p>
  <div class="t-name">John Smith</div>
  <div class="t-stars"><svg width="84" height="14" viewBox="0 0 84 14"><g fill="#f5a623"><polygon id="st" points="7,0 9,5 14,5 10,8 11.5,13 7,10 2.5,13 4,8 0,5 5,5"/><use href="#st" x="17"/><use href="#st" x="34"/><use href="#st" x="51"/><use href="#st" x="68"/></g></svg></div>
</div>
<div class="abs avatar" style="left:114px;top:2817px" role="img" aria-label="Portrait of a client"></div>

<div class="abs t-card" style="left:678px">
  <div class="t-quote">&ldquo;</div>
  <p class="t-text">Lorem ipsum dolor sit amet, consectetur adipiscing elit, sed do eiusmod tempor incididunt dolore magna aliqua.</p>
  <div class="t-name">John Doe</div>
  <div class="t-stars"><svg width="84" height="14" viewBox="0 0 84 14"><g fill="#f5a623"><use href="#st"/><use href="#st" x="17"/><use href="#st" x="34"/><use href="#st" x="51"/><use href="#st" x="68"/></g></svg></div>
</div>
<div class="abs avatar" style="left:624px;top:2817px" role="img" aria-label="Portrait of a client"></div>

<!-- contact -->
<svg class="abs contact-bg" width="1200" height="597" viewBox="0 0 1200 597">
  <rect width="1200" height="597" fill="#2c3b66"/>
  <polygon points="940,0 1200,0 1200,597 697,597" fill="#e3262f"/>
</svg>
<h2 class="abs heading contact-title">Contact Us</h2>
<div class="abs field" style="left:111px;top:3300px;width:232px;height:44px">First Name</div>
<div class="abs field" style="left:351px;top:3300px;width:233px;height:44px">Last Name</div>
<div class="abs field" style="left:111px;top:3355px;width:232px;height:44px">Message</div>
<div class="abs field" style="left:351px;top:3355px;width:233px;height:44px">Phone Number</div>
<div class="abs field" style="left:111px;top:3413px;width:473px;height:88px">Email Address</div>
<div class="btn" style="left:111px;top:3545px;width:169px;height:50px">Send Message <span class="dot"></span></div>
<div class="abs contact-frame"></div>
<div class="abs contact-photo" role="img" aria-label="Agent showing a couple a brick home"></div>
<div class="abs contact-frame-b"></div>
<div class="abs contact-frame-c"></div>
<div class="abs contact-badge"><div class="brand">Tallgrove<br>Vale</div></div>

<!-- footer -->
<div class="abs footer-logo"><div class="sq"></div><div class="brand">Tallgrove Vale<br>Management</div></div>
<div class="abs vline" style="left:415px;top:3755px;height:200px"></div>
<div class="abs vline" style="left:694px;top:3755px;height:200px"></div>
<div class="abs f-title" style="left:503px;top:3759px">Quick Links</div>
<ul class="abs f-links" style="left:503px;top:3796px"><li>Home</li><li>Services</li><li>About Us</li><li>Blog</li><li>Contact Us</li></ul>
<div class="abs f-title" style="left:774px;top:3759px">Contact Info</div>
<svg class="abs" style="left:776px;top:3800px" width="14" height="20" viewBox="0 0 14 20"><path d="M7 0a7 7 0 0 1 7 7c0 5-7 13-7 13S0 12 0 7a7 7 0 0 1 7-7z" fill="#e3262f"/><circle cx="7" cy="7" r="2.5" fill="#fff"/></svg>
<div class="abs f-info" style="left:805px;top:3796px;width:270px">2710 W. Orchard Ridge Rd. Ste 40 Maplewood, OH 43219</div>
<svg class="abs" style="left:775px;top:3864px" width="18" height="13" viewBox="0 0 18 13"><rect width="18" height="13" fill="#e3262f"/><polyline points="0,0 9,7 18,0" fill="none" stroke="#fff" stroke-width="1.5"/></svg>
<div class="abs f-info" style="left:805px;top:3859px">info@tallgrovevalemanagement.com</div>
<svg class="abs" style="left:776px;top:3903px" width="16" height="16" viewBox="0 0 16 16"><path d="M3 1l3 3-2 2c1 2 3 4 5 5l2-2 3 3-2 3C7 15 1 9 0 4z" fill="#e3262f"/></svg>
<div class="abs f-info" style="left:805px;top:3901px;text-decoration:underline">555.014.2290</div>
<div class="abs f-rule"></div>
<div class="abs f-legal" style="left:111px">&copy; 2026 Tallgrove Vale Management. All Rights Reserved.</div>
<div class="abs social" style="left:545px"></div>
<div class="abs social" style="left:585px"></div>
<div class="abs social" style="left:625px"></div>
<div class="abs f-legal" style="left:866px;word-spacing:2px">Privacy &nbsp;&nbsp;| &nbsp;&nbsp;Terms &nbsp;&nbsp;| &nbsp;&nbsp;Disclaimer</div>

</body>
</html>
```